Long term Care Provider Conference

Banner for LTC providers to know that they can rely on us to deliver high value, cost efficient, professional back office support to streamline operations, improve and maintain compliance with administrative and or nursing solutions for their agency.

Want to update the wording

```html
<!DOCTYPE html>
<html lang="en">
<head>
<meta charset="UTF-8">
<title>Verano Assist – Long-Term Care Provider Conference Banner</title>
<link href="https://fonts.googleapis.com/css2?family=Poppins:wght@400;500;600;700&display=swap" rel="stylesheet">
<style>
  :root {
    --stage: #2a2a2a;
    --paper: #f7f7f6;
    --teal: #5f8890;
    --teal-dark: #4c727a;
    --teal-light: #7fa3a9;
    --teal-text: #3f7079;
    --sand: #c8b7ad;
    --ink: #2f3b3e;
    --outline: #9aa3a5;
    --white: #ffffff;
  }
  * { box-sizing: border-box; margin: 0; padding: 0; }
  html, body { width: 667px; height: 1200px; overflow: hidden; }
  body {
    background: var(--stage);
    font-family: "Poppins", sans-serif;
    position: relative;
  }
  .banner {
    position: absolute;
    left: 28px; top: 268px;
    width: 610px; height: 663px;
    background: var(--paper);
    border-radius: 34px 34px 0 0;
    overflow: hidden;
    box-shadow: 0 14px 30px rgba(0,0,0,.45);
  }
  .tagline {
    position: absolute; left: 55px; top: 46px;
    font-size: 10.5px; font-weight: 600; letter-spacing: 1px;
    color: var(--ink);
    white-space: nowrap;
  }
  .hero {
    position: absolute; left: 35px; top: 72px;
    width: 540px; height: 230px;
    border-radius: 12px;
    background: linear-gradient(120deg, var(--teal-dark), var(--teal) 55%, var(--teal-light));
    overflow: hidden;
  }
  .hero-photo {
    position: absolute; right: 0; top: 0;
    width: 300px; height: 100%;
    background: linear-gradient(100deg, rgba(95,136,144,0) 0%, #8aa6a6 40%, #9a9a8a 80%, #8b7a66 100%);
  }
  .hero-title {
    position: absolute; left: 30px; top: 34px;
    font-size: 24px; line-height: 32px; font-weight: 700;
    color: var(--white);
    white-space: nowrap;
  }
  .logo-tab {
    position: absolute; left: 362px; top: 38px;
    width: 222px; height: 62px;
    background: var(--paper);
    border-radius: 0 0 0 30px;
    display: flex; align-items: center; gap: 8px;
    padding-left: 16px;
  }
  .logo-dot {
    width: 34px; height: 34px; border-radius: 50%;
    background: var(--teal);
    flex: none;
  }
  .logo-name {
    font-size: 22px; font-weight: 600; color: var(--ink);
    white-space: nowrap;
  }
  .stats { position: absolute; left: 58px; top: 328px; width: 200px; }
  .stat {
    display: flex; align-items: center; gap: 12px;
    height: 58px;
    border-bottom: 1.5px solid var(--ink);
  }
  .stat:last-child { border-bottom: none; }
  .stat-num {
    width: 72px; flex: none;
    font-size: 32px; font-weight: 500;
    color: transparent;
    -webkit-text-stroke: 1px var(--outline);
  }
  .stat-num b {
    color: var(--teal-text); -webkit-text-stroke: 0; font-weight: 700;
  }
  .stat-label {
    font-size: 13px; line-height: 17px; font-weight: 500; color: var(--teal-text);
    white-space: nowrap;
  }
  .services {
    position: absolute; left: 278px; top: 323px;
    width: 274px; height: 170px;
    background: var(--sand);
    border-radius: 12px;
  }
  .services-head {
    position: absolute; left: 0; top: -6px;
    width: 150px; height: 30px;
    background: var(--paper);
    border-radius: 0 0 16px 0;
    font-size: 14px; font-weight: 600; color: var(--teal-text);
    padding: 3px 0 0 40px;
    white-space: nowrap;
  }
  .service {
    position: absolute;
    display: flex; align-items: center; gap: 6px;
    font-size: 11px; line-height: 14px; color: var(--white); font-weight: 500;
    white-space: nowrap;
  }
  .service svg { flex: none; }
  .service span { border-left: 1px solid var(--white); padding-left: 5px; }
  .footer-band {
    position: absolute; left: 0; bottom: 0;
    width: 610px; height: 122px;
    background: linear-gradient(90deg, var(--teal-dark), var(--teal) 60%, var(--teal-light));
  }
  .claim-tab {
    position: absolute; left: 60px; top: 528px;
    width: 490px; height: 32px;
    background: var(--paper);
    border-radius: 0 0 18px 18px;
    text-align: center;
    font-size: 11px; font-weight: 600; letter-spacing: 2.2px;
    color: var(--teal-text);
    padding-top: 8px;
    white-space: nowrap;
  }
  .contacts {
    position: absolute; left: 0; top: 576px; width: 610px;
    text-align: center;
    font-size: 11.5px; color: var(--white);
    white-space: nowrap;
  }
  .contacts .sep { margin: 0 10px; opacity: .8; }
</style>
</head>
<body>
  <main class="banner">
    <p class="tagline">BACK OFFICE SUPPORT FOR LONG-TERM CARE</p>

    <section class="hero">
      <div class="hero-photo" role="img" aria-label="Smiling healthcare virtual assistant wearing a headset and white coat"></div>
      <h1 class="hero-title">Streamline Your<br>LTC Agency with<br>Expert Back Office<br>&amp; Nursing Support<br>You Can Rely On</h1>
    </section>

    <div class="logo-tab">
      <div class="logo-dot"></div>
      <span class="logo-name">Verano Assist</span>
    </div>

    <section class="stats">
      <div class="stat"><span class="stat-num">98<b>%</b></span><span class="stat-label">Client<br>Satisfaction</span></div>
      <div class="stat"><span class="stat-num">45<b>k</b></span><span class="stat-label">Hours of<br>Support provided</span></div>
      <div class="stat"><span class="stat-num">20<b>+</b></span><span class="stat-label">Years of<br>Business Expertise</span></div>
    </section>

    <section class="services">
      <h2 class="services-head">Our Services</h2>
      <div class="service" style="left:24px;top:38px;">
        <svg width="18" height="20" viewBox="0 0 18 20" fill="none" stroke="#fff" stroke-width="1.2"><circle cx="9" cy="6" r="4"/><path d="M2 19c0-4 3-7 7-7s7 3 7 7"/></svg>
        <span>Registered<br>Nurse</span>
      </div>
      <div class="service" style="left:148px;top:38px;">
        <svg width="18" height="20" viewBox="0 0 18 20" fill="none" stroke="#fff" stroke-width="1.2"><rect x="2" y="1" width="14" height="18" rx="2"/><path d="M5 6h8M5 10h8M5 14h5"/></svg>
        <span>Medical<br>Billing</span>
      </div>
      <div class="service" style="left:24px;top:81px;">
        <svg width="18" height="20" viewBox="0 0 18 20" fill="none" stroke="#fff" stroke-width="1.2"><circle cx="9" cy="10" r="3"/><circle cx="9" cy="10" r="7" stroke-dasharray="3 2"/></svg>
        <span>Administrative<br>Support</span>
      </div>
      <div class="service" style="left:148px;top:81px;">
        <svg width="20" height="20" viewBox="0 0 20 20" fill="none" stroke="#fff" stroke-width="1.2"><circle cx="10" cy="10" r="9"/><path d="M6 10l3 3 5-6"/></svg>
        <span>Compliance<br>Support</span>
      </div>
      <div class="service" style="left:24px;top:124px;">
        <svg width="18" height="20" viewBox="0 0 18 20" fill="none" stroke="#fff" stroke-width="1.2"><rect x="2" y="2" width="12" height="16" rx="1"/><path d="M5 7h6M5 11h4"/><circle cx="14" cy="15" r="3"/></svg>
        <span>Case<br>Management</span>
      </div>
    </section>

    <div class="footer-band"></div>
    <p class="claim-tab">HIGH VALUE, COST-EFFICIENT, COMPLIANT SUPPORT</p>
    <p class="contacts">www.veranoassist.com<span class="sep">|</span>info@veranoassist.com<span class="sep">|</span>+281-555-0147</p>
  </main>
</body>
</html>
```